Quarry Meadow Half Marathon 2015

I am in need of a 2 sided promotional print postcard for our half marathon held in March. The print is distributed in October.

Must include running stick figure, Corvell Gap Bridge and lighthouse in design. These elements can be seen in the uploaded design from last year. Also, the Brookfane Striders Logo and Dunmore logo must be on it.

Saturday, March 21st at 9:30am
Register on RACEPLOT.com
Register before end of 2014 and recieve $5 off registration - Use coupon code QM7408

Back of the post card to include details:

Registration fee $60 until 3/13/14, race day $70
Race start/finish is walking distance from the train -Transit East Kellan Line to Oakhaven Station
Finisher Goodie bag
LS technical shirt
Electronic timing
NRAQB Certified course
Water and Fizzlyte fluid stations
CASH awards to top 3 overall male and female finishers
Awards and prizes to top category finishers
Each finisher will receive a 2014 Quarry Meadow Half Marathon medal, sponsored by Dunmore Regional Hospital Center

Target Market(s)

These are males and females ages 21-55

Industry/Entity Type

Electronic

Colors
33a6d7
34b8a4
faee3f
add136
3176b5
f04a50

Requirements
Must have
• 2 logos
name - Quarry Meadow Half Marathon
date
www.brookfanestriders.example
2 sided with detailed info on back and general info on front

```html
<!DOCTYPE html>
<html lang="en">
<head>
<meta charset="utf-8">
<title>Quarry Meadow Half Marathon – Postcard Back</title>
<link href="https://fonts.googleapis.com/css2?family=Kaushan+Script&family=Questrial&family=Mulish:wght@800&family=Arvo&display=swap" rel="stylesheet">
<style>
  :root {
    --paper: #ffffff;
    --lime: #add136;
    --blue: #3176b5;
    --sky: #33a6d7;
    --coral: #f04a50;
    --ink: #111111;
    --rule: #555555;
    --forest: #1f4a2c;
  }
  html, body {
    margin: 0;
    padding: 0;
    overflow: hidden;
    background: var(--paper);
  }
  .postcard {
    position: relative;
    width: 1200px;
    height: 777px;
    background: var(--paper);
    overflow: hidden;
    font-family: "Questrial", "Century Gothic", sans-serif;
  }
  .greeting {
    position: absolute;
    left: 36px;
    top: 22px;
    margin: 0;
    font-family: "Kaushan Script", cursive;
    font-weight: 400;
    font-size: 40px;
    color: var(--lime);
    letter-spacing: 1px;
  }
  .greeting-swash {
    position: absolute;
    left: 45px;
    top: 76px;
  }
  .race-photo {
    position: absolute;
    left: 117px;
    top: 77px;
    width: 381px;
    height: 187px;
    border: 5px solid #fff;
    box-shadow: 0 2px 6px rgba(0,0,0,0.35);
    transform: rotate(-1.2deg);
    background: linear-gradient(180deg, #9aa4b4 0%, #b9c2ce 38%, #6f5d55 62%, #3e3a3c 82%, #5a5b60 100%);
  }
  .stamp-box {
    position: absolute;
    left: 1015px;
    top: 19px;
    width: 176px;
    height: 175px;
    border: 1px solid var(--rule);
    box-sizing: border-box;
  }
  .divider {
    position: absolute;
    left: 605px;
    top: 84px;
    width: 3px;
    height: 548px;
    background: var(--ink);
  }
  .address-line {
    position: absolute;
    left: 682px;
    width: 444px;
    height: 1px;
    background: var(--rule);
  }
  .details {
    position: absolute;
    left: 31px;
    top: 280px;
    width: 580px;
    color: var(--blue);
  }
  .fee {
    margin: 0;
    font-family: "Mulish", "Century Gothic", sans-serif;
    font-weight: 800;
    font-size: 21.5px;
  }
  .transit {
    margin: 10px 0 0;
    font-size: 21px;
    line-height: 26px;
  }
  .perks {
    list-style: none;
    margin: 16px 0 0 60px;
    padding: 0;
    font-size: 21px;
  }
  .perks li {
    position: relative;
    height: 31.8px;
    padding-left: 14px;
  }
  .perks li::before {
    content: "";
    position: absolute;
    left: -1px;
    top: 7px;
    width: 11px;
    height: 11px;
    border-radius: 50%;
    background: var(--lime);
  }
  .medal-note {
    margin: 8px 0 0;
    font-family: "Arvo", Georgia, serif;
    font-size: 19px;
    line-height: 26px;
    color: var(--coral);
  }
  .sponsor {
    position: absolute;
    left: 44px;
    top: 697px;
    font-size: 18px;
    color: var(--forest);
  }
  .club {
    position: absolute;
    left: 365px;
    top: 679px;
    display: flex;
    align-items: center;
    gap: 14px;
    font-size: 20px;
    color: var(--sky);
  }
  .club-mark {
    width: 70px;
    height: 65px;
    border-radius: 4px;
    background: var(--sky);
  }
</style>
</head>
<body>
<main class="postcard">
  <h1 class="greeting">Wish You Were Here!!</h1>
  <svg class="greeting-swash" width="130" height="32" viewBox="0 0 130 32" aria-hidden="true">
    <path d="M4 28 C 40 14, 90 8, 122 7" fill="none" stroke="#add136" stroke-width="4" stroke-linecap="round"/>
  </svg>

  <div class="race-photo" role="img" aria-label="Photo of runners crowding the start line on a road beside a wide river with a long bridge in the distance"></div>

  <div class="stamp-box"></div>
  <div class="divider"></div>

  <div class="address-line" style="top:407px"></div>
  <div class="address-line" style="top:465px"></div>
  <div class="address-line" style="top:522px"></div>
  <div class="address-line" style="top:578px"></div>

  <section class="details">
    <p class="fee">Registration fee $60 until 3/13/14, race day $70</p>
    <p class="transit">Race start/finish is walking distance from<br>the train -Transit East Kellan Line to Oakhaven Station</p>
    <ul class="perks">
      <li>Finisher Goodie bag</li>
      <li>LS technical shirt</li>
      <li>Electronic timing</li>
      <li>NRAQB Certified course</li>
      <li>Water and Fizzlyte fluid stations</li>
      <li>Awards and prizes to top category finishers</li>
    </ul>
    <p class="medal-note">Each finisher will receive a 2014 Quarry Meadow<br>Half Marathon medal, sponsored by Dunmore<br>Regional Hospital Center</p>
  </section>

  <div class="sponsor">Dunmore Regional Hospital Center</div>
  <div class="club"><span class="club-mark"></span><span>Brookfane Striders</span></div>
</main>
</body>
</html>
```